Re Brand for Australian health food company

We have are looking to revamp our brand including the look of our packaging. We use vertical Doy packs - Kraft Paper - Dimension of pack for fruit and berry products is 125mm W x 210mm H
Our chocolate coated products are packed in bags 125mm W x 170mm H
We are looking for natural, moderns simplistic packaging. We would like a see-through window on the front of ALL PACKAGING. The window should occupy approx 30% to 40% of the entire front of package. Designers need to consider that the existing Mxvitalbites logo can be modified slightly - but we DO NOT need a new logo. Designers also need to understand that the aesthetic must be able to be applied to all marketing materials - business cards, company letter head, e mail signatures, advertisements, fliers , our new web site (yet to be designed) and social media web sites.

Target Market(s)

Health conscious consumers, families, hipsters, athletes

Font styles to use
Serif
Sans Serif

Colors
87cfc6
85cae6
cadf82
fbf289
f59195
fbc994

Requirements
Must have
• Our existing company logo (can be modified)
• Product name - see our web site for all products - no names will be changed
• Ingredients
• Vegan friendly logo or clearly stated
• No preservatives
• No added sugar
Nice to have
• Clean, crisp modern font.
• Printing both sides f bags (rear of bags contains information associated with food products.
Should not have
• High gloss or reflective look.

```html
<!DOCTYPE html>
<html lang="en">
<head>
<meta charset="utf-8">
<title>Mxvitalbites – Organic Dark Chocolate Range</title>
<link rel="stylesheet" href="https://fonts.googleapis.com/css2?family=Playfair+Display:ital,wght@1,700;1,900&family=Caveat:wght@600;700&family=Open+Sans:wght@400;600&display=swap">
<style>
  :root {
    --backdrop-top: #8d8d8d;
    --backdrop-mid: #c9c9c9;
    --backdrop-light: #f2f2f2;
    --kraft: #d9d0c4;
    --kraft-shade: #c4baad;
    --zip: #b5aa9c;
    --ink: #1e1a18;
    --logo-red: #b3201f;
    --vegan-green: #2c8a3c;
    --seal-gold: #c8a55c;
    --seal-gold-dark: #8e6e2c;
    --title-gold: #dcc57e;
    --claim-cream: #f3e4b0;
    --choc-light: #b6805e;
    --choc-dark: #4a2618;
    --rasp-light: #f0307f;
    --rasp-dark: #8c1459;
    --rasp-fruit: #e8406a;
    --blue-light: #2f8fe0;
    --blue-dark: #2a1a86;
    --blue-frame: #1f3f9a;
    --blue-fruit: #3d4f9a;
  }
  html, body {
    margin: 0;
    padding: 0;
    width: 1200px;
    height: 1200px;
    overflow: hidden;
  }
  body {
    background: radial-gradient(ellipse 70% 55% at 50% 78%, var(--backdrop-light) 0%, var(--backdrop-mid) 55%, var(--backdrop-top) 100%);
    font-family: "Open Sans", sans-serif;
  }
  .range {
    position: absolute;
    top: 230px;
    left: 0;
    width: 1200px;
    display: flex;
    justify-content: center;
    gap: 130px;
  }
  .pack {
    width: 450px;
    height: 650px;
    display: block;
  }
  .brand-name { font-family: "Open Sans", sans-serif; font-weight: 600; font-size: 11px; fill: var(--logo-red); letter-spacing: 0.3px; }
  .vegan-word { font-family: "Caveat", cursive; font-weight: 700; font-size: 30px; fill: #fff; }
  .vegan-sub { font-family: "Open Sans", sans-serif; font-weight: 600; font-size: 12px; fill: #fff; }
  .title-organic { font-family: "Playfair Display", serif; font-style: italic; font-weight: 700; font-size: 30px; }
  .title-fruit { font-family: "Playfair Display", serif; font-style: italic; font-weight: 900; fill: var(--title-gold); }
  .tagline { font-family: "Caveat", cursive; font-weight: 700; font-size: 46px; fill: var(--ink); }
  .tagline-reflect { font-family: "Caveat", cursive; font-weight: 700; font-size: 46px; opacity: 0.22; }
  .net-weight { font-family: "Playfair Display", serif; font-size: 15px; fill: var(--ink); }
  .claim { font-family: "Playfair Display", serif; font-style: italic; font-weight: 700; font-size: 15px; fill: var(--claim-cream); }
  .nutri-label { font-family: "Open Sans", sans-serif; font-size: 4.5px; fill: var(--ink); }
  .nutri-value { font-family: "Open Sans", sans-serif; font-weight: 600; font-size: 7px; fill: var(--ink); }
  .nutri-pct { font-family: "Open Sans", sans-serif; font-weight: 600; font-size: 4.5px; fill: #fff; }
</style>
</head>
<body>
<main class="range">

  <svg class="pack pack--raspberry" viewBox="0 0 450 650" xmlns="http://www.w3.org/2000/svg" aria-label="Organic Raspberries dark chocolate pack">
    <defs>
      <linearGradient id="rasp-banner" x1="0" y1="0" x2="1" y2="1">
        <stop offset="0" stop-color="var(--rasp-light)"/>
        <stop offset="1" stop-color="var(--rasp-dark)"/>
      </linearGradient>
      <linearGradient id="kraft-side" x1="0" x2="1">
        <stop offset="0" stop-color="var(--kraft-shade)"/>
        <stop offset="0.08" stop-color="var(--kraft)"/>
        <stop offset="0.92" stop-color="var(--kraft)"/>
        <stop offset="1" stop-color="var(--kraft-shade)"/>
      </linearGradient>
      <radialGradient id="choc-fill" cx="0.5" cy="0.4" r="0.8">
        <stop offset="0" stop-color="var(--choc-light)"/>
        <stop offset="1" stop-color="var(--choc-dark)"/>
      </radialGradient>
      <clipPath id="rasp-window-clip">
        <path d="M420 410 C340 406 262 416 230 442 C184 482 188 570 222 610 L420 610 Z"/>
      </clipPath>
      <clipPath id="rasp-reflect-clip">
        <rect x="90" y="362" width="300" height="30"/>
      </clipPath>
    </defs>

    <rect class="pack-body" x="0" y="0" width="450" height="650" rx="10" fill="url(#kraft-side)"/>
    <line class="zip-line" x1="25" y1="50" x2="425" y2="50" stroke="var(--zip)" stroke-width="3"/>

    <g class="brand-logo">
      <circle cx="225" cy="105" r="10" fill="var(--logo-red)"/>
      <text class="brand-name" x="225" y="140" text-anchor="middle">Mxvitalbites</text>
    </g>

    <g class="vegan-badge">
      <circle cx="72" cy="160" r="42" fill="var(--vegan-green)"/>
      <text class="vegan-word" x="72" y="160" text-anchor="middle">Vegan</text>
      <text class="vegan-sub" x="80" y="180" text-anchor="middle">Friendly</text>
    </g>

    <g class="quality-seal">
      <circle cx="362" cy="145" r="48" fill="var(--seal-gold)"/>
      <circle cx="362" cy="145" r="38" fill="none" stroke="var(--seal-gold-dark)" stroke-width="2"/>
      <circle cx="362" cy="145" r="20" fill="var(--choc-dark)"/>
    </g>

    <g class="title-banner">
      <path d="M100 195 C170 170 260 215 360 190 C395 182 398 230 385 262 C372 292 300 285 220 298 C150 308 100 325 88 300 C82 270 95 230 100 195 Z" fill="url(#rasp-banner)" stroke="#f6c3dd" stroke-width="2"/>
      <text class="title-organic" x="240" y="232" text-anchor="middle" fill="#e9d8f2">Organic</text>
      <text class="title-fruit" x="240" y="282" text-anchor="middle" font-size="46">Raspberries</text>
    </g>

    <g class="tagline-group">
      <text class="tagline" x="240" y="350" text-anchor="middle">Dark chocolate</text>
      <line x1="95" y1="358" x2="385" y2="358" stroke="var(--ink)" stroke-width="1.2"/>
      <g clip-path="url(#rasp-reflect-clip)">
        <text class="tagline-reflect" x="240" y="-366" text-anchor="middle" transform="scale(1,-1)" fill="var(--rasp-light)">Dark chocolate</text>
      </g>
    </g>

    <rect class="chocolate-window" x="180" y="400" width="245" height="215" fill="url(#choc-fill)" clip-path="url(#rasp-window-clip)" role="img" aria-label="See-through window showing chocolate coated raspberries"/>
    <path class="window-frame" d="M425 406 C340 401 258 412 225 438 C178 480 182 572 218 614" fill="none" stroke="var(--rasp-dark)" stroke-width="8" stroke-linecap="round"/>

    <ellipse class="fruit-illustration" cx="150" cy="475" rx="90" ry="55" fill="var(--rasp-fruit)" role="img" aria-label="Illustration of fresh raspberries with a leaf"/>

    <g class="claims">
      <rect x="245" y="530" width="155" height="58" fill="rgba(40,20,12,0.35)" stroke="var(--claim-cream)" stroke-width="1"/>
      <line x1="245" y1="559" x2="400" y2="559" stroke="var(--claim-cream)" stroke-width="0.8"/>
      <path d="M252 545 l4 5 l8 -10" fill="none" stroke="var(--claim-cream)" stroke-width="1.6"/>
      <text class="claim" x="268" y="550">No preservatives</text>
      <path d="M252 574 l4 5 l8 -10" fill="none" stroke="var(--claim-cream)" stroke-width="1.6"/>
      <text class="claim" x="268" y="580">No added sugar</text>
    </g>

    <text class="net-weight" x="72" y="552">125g Net</text>
    <g class="nutrition-strip" transform="translate(72,560)">
      <g><rect width="22" height="34" rx="3" fill="none" stroke="var(--ink)" stroke-width="0.8"/><text class="nutri-label" x="11" y="8" text-anchor="middle">Sugars</text><text class="nutri-value" x="11" y="19" text-anchor="middle">0,5g</text><circle cx="11" cy="27" r="5.5" fill="var(--ink)"/><text class="nutri-pct" x="11" y="28.6" text-anchor="middle">1%</text></g>
      <g transform="translate(26,0)"><rect width="22" height="34" rx="3" fill="none" stroke="var(--ink)" stroke-width="0.8"/><text class="nutri-label" x="11" y="8" text-anchor="middle">Fat</text><text class="nutri-value" x="11" y="19" text-anchor="middle">7,3g</text><circle cx="11" cy="27" r="5.5" fill="var(--ink)"/><text class="nutri-pct" x="11" y="28.6" text-anchor="middle">10%</text></g>
      <g transform="translate(52,0)"><rect width="22" height="34" rx="3" fill="none" stroke="var(--ink)" stroke-width="0.8"/><text class="nutri-label" x="11" y="8" text-anchor="middle">Sat fat</text><text class="nutri-value" x="11" y="19" text-anchor="middle">1,7g</text><circle cx="11" cy="27" r="5.5" fill="var(--ink)"/><text class="nutri-pct" x="11" y="28.6" text-anchor="middle">9%</text></g>
      <g transform="translate(78,0)"><rect width="22" height="34" rx="3" fill="none" stroke="var(--ink)" stroke-width="0.8"/><text class="nutri-label" x="11" y="8" text-anchor="middle">Salt</text><text class="nutri-value" x="11" y="19" text-anchor="middle">0,2g</text><circle cx="11" cy="27" r="5.5" fill="var(--ink)"/><text class="nutri-pct" x="11" y="28.6" text-anchor="middle">8%</text></g>
    </g>
  </svg>

  <svg class="pack pack--blueberry" viewBox="0 0 450 650" xmlns="http://www.w3.org/2000/svg" aria-label="Organic Blueberry dark chocolate pack">
    <defs>
      <linearGradient id="blue-banner" x1="0" y1="0" x2="1" y2="1">
        <stop offset="0" stop-color="var(--blue-light)"/>
        <stop offset="1" stop-color="var(--blue-dark)"/>
      </linearGradient>
      <linearGradient id="kraft-side-b" x1="0" x2="1">
        <stop offset="0" stop-color="var(--kraft-shade)"/>
        <stop offset="0.08" stop-color="var(--kraft)"/>
        <stop offset="0.92" stop-color="var(--kraft)"/>
        <stop offset="1" stop-color="var(--kraft-shade)"/>
      </linearGradient>
      <radialGradient id="choc-fill-b" cx="0.5" cy="0.4" r="0.8">
        <stop offset="0" stop-color="var(--choc-light)"/>
        <stop offset="1" stop-color="var(--choc-dark)"/>
      </radialGradient>
      <clipPath id="blue-window-clip">
        <path d="M420 410 C340 406 262 416 230 442 C184 482 188 570 222 610 L420 610 Z"/>
      </clipPath>
      <clipPath id="blue-reflect-clip">
        <rect x="90" y="362" width="300" height="30"/>
      </clipPath>
    </defs>

    <rect class="pack-body" x="0" y="0" width="450" height="650" rx="10" fill="url(#kraft-side-b)"/>
    <line class="zip-line" x1="25" y1="50" x2="425" y2="50" stroke="var(--zip)" stroke-width="3"/>

    <g class="brand-logo">
      <circle cx="225" cy="105" r="10" fill="var(--logo-red)"/>
      <text class="brand-name" x="225" y="140" text-anchor="middle">Mxvitalbites</text>
    </g>

    <g class="vegan-badge">
      <circle cx="72" cy="160" r="42" fill="var(--vegan-green)"/>
      <text class="vegan-word" x="72" y="160" text-anchor="middle">Vegan</text>
      <text class="vegan-sub" x="80" y="180" text-anchor="middle">Friendly</text>
    </g>

    <g class="quality-seal">
      <circle cx="362" cy="145" r="48" fill="var(--seal-gold)"/>
      <circle cx="362" cy="145" r="38" fill="none" stroke="var(--seal-gold-dark)" stroke-width="2"/>
      <circle cx="362" cy="145" r="20" fill="var(--blue-fruit)"/>
    </g>

    <g class="title-banner">
      <path d="M100 195 C170 170 260 215 360 190 C395 182 398 230 385 262 C372 292 300 285 220 298 C150 308 100 325 88 300 C82 270 95 230 100 195 Z" fill="url(#blue-banner)" stroke="#bfe3fb" stroke-width="2"/>
      <text class="title-organic" x="240" y="232" text-anchor="middle" fill="#a9d8f5">Organic</text>
      <text class="title-fruit" x="240" y="282" text-anchor="middle" font-size="48">Blueberry</text>
    </g>

    <g class="tagline-group">
      <text class="tagline" x="240" y="350" text-anchor="middle">Dark chocolate</text>
      <line x1="95" y1="358" x2="385" y2="358" stroke="var(--ink)" stroke-width="1.2"/>
      <g clip-path="url(#blue-reflect-clip)">
        <text class="tagline-reflect" x="240" y="-366" text-anchor="middle" transform="scale(1,-1)" fill="var(--blue-dark)">Dark chocolate</text>
      </g>
    </g>

    <rect class="chocolate-window" x="180" y="400" width="245" height="215" fill="url(#choc-fill-b)" clip-path="url(#blue-window-clip)" role="img" aria-label="See-through window showing chocolate coated blueberries"/>
    <path class="window-frame" d="M425 406 C340 401 258 412 225 438 C178 480 182 572 218 614" fill="none" stroke="var(--blue-frame)" stroke-width="8" stroke-linecap="round"/>

    <ellipse class="fruit-illustration" cx="148" cy="477" rx="84" ry="55" fill="var(--blue-fruit)" role="img" aria-label="Illustration of fresh blueberries with leaves"/>

    <g class="claims">
      <rect x="245" y="530" width="155" height="58" fill="rgba(40,20,12,0.35)" stroke="var(--claim-cream)" stroke-width="1"/>
      <line x1="245" y1="559" x2="400" y2="559" stroke="var(--claim-cream)" stroke-width="0.8"/>
      <path d="M252 545 l4 5 l8 -10" fill="none" stroke="var(--claim-cream)" stroke-width="1.6"/>
      <text class="claim" x="268" y="550">No preservatives</text>
      <path d="M252 574 l4 5 l8 -10" fill="none" stroke="var(--claim-cream)" stroke-width="1.6"/>
      <text class="claim" x="268" y="580">No added sugar</text>
    </g>

    <text class="net-weight" x="72" y="556">125g Net</text>
    <g class="nutrition-strip" transform="translate(72,564)">
      <g><rect width="22" height="34" rx="3" fill="none" stroke="var(--ink)" stroke-width="0.8"/><text class="nutri-label" x="11" y="8" text-anchor="middle">Sugars</text><text class="nutri-value" x="11" y="19" text-anchor="middle">0,5g</text><circle cx="11" cy="27" r="5.5" fill="var(--ink)"/><text class="nutri-pct" x="11" y="28.6" text-anchor="middle">1%</text></g>
      <g transform="translate(26,0)"><rect width="22" height="34" rx="3" fill="none" stroke="var(--ink)" stroke-width="0.8"/><text class="nutri-label" x="11" y="8" text-anchor="middle">Fat</text><text class="nutri-value" x="11" y="19" text-anchor="middle">7,3g</text><circle cx="11" cy="27" r="5.5" fill="var(--ink)"/><text class="nutri-pct" x="11" y="28.6" text-anchor="middle">10%</text></g>
      <g transform="translate(52,0)"><rect width="22" height="34" rx="3" fill="none" stroke="var(--ink)" stroke-width="0.8"/><text class="nutri-label" x="11" y="8" text-anchor="middle">Sat fat</text><text class="nutri-value" x="11" y="19" text-anchor="middle">1,7g</text><circle cx="11" cy="27" r="5.5" fill="var(--ink)"/><text class="nutri-pct" x="11" y="28.6" text-anchor="middle">9%</text></g>
      <g transform="translate(78,0)"><rect width="22" height="34" rx="3" fill="none" stroke="var(--ink)" stroke-width="0.8"/><text class="nutri-label" x="11" y="8" text-anchor="middle">Salt</text><text class="nutri-value" x="11" y="19" text-anchor="middle">0,2g</text><circle cx="11" cy="27" r="5.5" fill="var(--ink)"/><text class="nutri-pct" x="11" y="28.6" text-anchor="middle">8%</text></g>
    </g>
  </svg>

</main>
</body>
</html>
```